Brackenmoor Grounds require a modern, vibrant Logo with accompanying flyer design to represent their

Brackenmoor Grounds require an exciting, vibrant and modern Logo and accompanying flyer design to represent their new brand as Sussex based, ground works, landscaping and Garden Care business.

We really want to appeal to local residential and business customers that require top quality landscaping services.

Target Market(s)

Residential customers needing their garden care and landscaping, fencing, patios pathways, or decking. Business customers requiring major landscaping, driveways, digging etc.

Industry/Entity Type

Landscape Gardening

Logo Text

Brackenmoor Grounds

Font styles to use
Sans Serif
Decorative
Script

Requirements
Must have
• Be bright, modern slick and slightly playful. Possibly to have a strap line with regards to the fact we are 'The Local Landscaping Experts' or 'Ground Works | Landscaping | Garden Care' or something along those lines.
• Flyer needs to be size A5 and be double sided, full colour, one side must have a really nice landscape image and the new logo (yet to be designed) and the other a really nice image with the following details:
• web: www.brackenmoorgrounds.co.uk
• email: dale@brackenmoorgrounds.co.uk
• Tel: 07952 418260
• For all of your Landscape and Groundwork needs..
Nice to have
• A memorable logo with a relevant icon that is very modern and clean.

```html
<!DOCTYPE html>
<html lang="en">
<head>
<meta charset="utf-8">
<title>Brackenmoor Grounds – A5 Flyer</title>
<link href="https://fonts.googleapis.com/css2?family=Cinzel:wght@400;700&family=Arimo:wght@400;700&display=swap" rel="stylesheet">
<style>
  :root {
    --backdrop: #a9a9aa;
    --brown-deep: #3f2413;
    --brown: #5b3a22;
    --brown-light: #6f4a2c;
    --green: #7ab533;
    --green-mid: #5c9d2c;
    --green-dark: #2f6a1a;
    --hedge: #3f8a26;
    --lime: #c9d94a;
    --paving: #b3aca3;
    --mower-red: #d8332c;
    --bloom: #d8487a;
    --white: #ffffff;
    --ink: #666666;
  }
  * { box-sizing: border-box; margin: 0; padding: 0; }
  html, body { width: 880px; height: 1200px; overflow: hidden; }
  body { background: var(--backdrop); position: relative; font-family: "Arimo", Arial, sans-serif; }

  .side { position: absolute; left: 70px; width: 742px; overflow: hidden; box-shadow: 0 1px 3px rgba(0,0,0,0.25); }
  .side--front { top: 72px; height: 522px; }
  .side--back { top: 607px; height: 523px; background: var(--white); }

  /* Front */
  .garden-photo {
    position: absolute; inset: 0;
    background:
      radial-gradient(ellipse 22% 14% at 62% 38%, var(--lime) 0%, rgba(201,217,74,0) 100%),
      radial-gradient(ellipse 60% 16% at 52% 72%, var(--paving) 0%, rgba(179,172,163,0.55) 55%, rgba(179,172,163,0) 100%),
      radial-gradient(ellipse 12% 40% at 22% 30%, rgba(179,172,163,0.85) 0%, rgba(179,172,163,0) 100%),
      radial-gradient(ellipse 30% 20% at 85% 90%, #7cbd45 0%, rgba(124,189,69,0) 100%),
      radial-gradient(ellipse 35% 25% at 15% 85%, #2a6a1a 0%, rgba(42,106,26,0) 100%),
      linear-gradient(165deg, #2c7020 0%, var(--hedge) 35%, #4f9a2e 60%, #27601a 100%);
  }
  .ribbon { position: absolute; left: 0; top: 198px; width: 375px; height: 127px; filter: drop-shadow(0 3px 4px rgba(0,0,0,0.35)); }
  .ribbon svg { position: absolute; inset: 0; }

  .brand { position: absolute; display: flex; align-items: center; }
  .brand__mark {
    flex: none; border-radius: 50%;
    background: var(--green);
    border: 4px solid var(--white);
    box-shadow: 0 0 0 3px var(--brown-deep), 0 0 0 5px var(--white);
  }
  .brand__name { font-family: "Cinzel", "Times New Roman", serif; font-weight: 400; color: var(--white); line-height: 1.02; }
  .brand__tag { font-family: "Arimo", Arial, sans-serif; color: var(--white); font-size: 8px; margin-top: 7px; display: flex; align-items: center; gap: 5px; }
  .brand__tag::before, .brand__tag::after { content: ""; width: 20px; height: 1px; background: var(--white); }

  .ribbon .brand { left: 26px; top: 16px; }
  .ribbon .brand__mark { width: 92px; height: 92px; }
  .ribbon .brand__text { margin-left: 18px; }
  .ribbon .brand__name { font-size: 25px; }

  /* Back */
  .mower-photo {
    position: absolute; left: 320px; top: 0; width: 422px; height: 152px;
    background:
      radial-gradient(ellipse 20% 34% at 68% 58%, var(--mower-red) 0%, rgba(216,51,44,0.6) 50%, rgba(216,51,44,0) 100%),
      radial-gradient(ellipse 60% 12% at 55% 14%, #e3c64f 0%, rgba(227,198,79,0) 100%),
      linear-gradient(180deg, #8fbf4a 0%, var(--green-mid) 40%, #7ab63e 100%);
  }
  .mower-photo::after {
    content: ""; position: absolute; inset: 0;
    background: linear-gradient(90deg, #fff 0%, rgba(255,255,255,0.75) 18%, rgba(255,255,255,0) 42%);
  }
  .headline {
    position: absolute; left: 31px; top: 30px;
    font-family: "Cinzel", "Times New Roman", serif; font-weight: 700;
    font-size: 30px; line-height: 33px; color: var(--brown-deep);
  }
  .headline .accent { color: var(--green); }
  .intro { position: absolute; left: 31px; top: 136px; width: 332px; color: var(--ink); font-size: 14.6px; line-height: 17.6px; }
  .intro p + p { margin-top: 9px; }

  .service-band {
    position: absolute; left: 385px; top: 152px; width: 357px; height: 40px;
    background: var(--brown); color: var(--white); font-weight: 700; font-size: 14.5px;
    display: flex; align-items: center; justify-content: center;
  }
  .flower-photo { position: absolute; top: 196px; height: 133px; }
  .flower-photo--beds {
    left: 385px; width: 175px;
    background:
      radial-gradient(ellipse 40% 25% at 30% 45%, var(--bloom) 0%, rgba(216,72,122,0) 100%),
      radial-gradient(ellipse 35% 20% at 65% 35%, #e2c04a 0%, rgba(226,192,74,0) 100%),
      radial-gradient(ellipse 40% 18% at 55% 75%, #f1ede0 0%, rgba(241,237,224,0) 100%),
      linear-gradient(180deg, #8ab254 0%, #4f9a2c 60%, #5aa632 100%);
  }
  .flower-photo--lawn {
    left: 565px; width: 177px;
    background:
      radial-gradient(ellipse 45% 14% at 40% 48%, var(--bloom) 0%, rgba(216,72,122,0) 100%),
      radial-gradient(ellipse 40% 20% at 60% 18%, #b86a3a 0%, rgba(184,106,58,0) 100%),
      linear-gradient(180deg, #d9d6c8 0%, #5f8a34 28%, #4f8a2a 45%, #6db33a 65%, #86c63f 100%);
  }

  .footer-panel {
    position: absolute; left: 0; top: 333px; width: 742px; height: 190px;
    background: radial-gradient(ellipse 70% 90% at 45% 45%, var(--brown-light) 0%, var(--brown) 50%, var(--brown-deep) 100%);
  }
  .services-tab { position: absolute; left: 0; top: 0; width: 290px; height: 28px; }
  .services-tab svg { position: absolute; inset: 0; }
  .services-tab span { position: absolute; left: 24px; top: 6px; color: var(--white); font-weight: 700; font-size: 14.5px; }
  .services { list-style: none; position: absolute; left: 29px; top: 38px; color: var(--white); font-weight: 700; font-size: 13px; }
  .services li { display: flex; align-items: center; height: 20.5px; gap: 6px; }
  .services li svg { flex: none; }
  .services .pair { display: inline-flex; align-items: center; gap: 6px; margin-left: 2px; }

  .footer-panel .brand { left: 378px; top: 5px; }
  .footer-panel .brand__mark { width: 96px; height: 96px; }
  .footer-panel .brand__text { margin-left: 22px; }
  .footer-panel .brand__name { font-size: 27px; }

  .contact { list-style: none; position: absolute; left: 500px; top: 118px; color: var(--white); font-weight: 700; font-size: 12.5px; }
  .contact li { display: flex; align-items: center; gap: 6px; height: 15.5px; }
</style>
</head>
<body>

<section class="side side--front">
  <div class="garden-photo" role="img" aria-label="Photograph of a formal knot garden with clipped box hedges, topiary columns and curving block-paved paths"></div>
  <div class="ribbon">
    <svg width="375" height="127" viewBox="0 0 375 127" aria-hidden="true">
      <defs>
        <linearGradient id="ribbonFill" x1="0" x2="1">
          <stop offset="0" stop-color="#5b3a22"/><stop offset="1" stop-color="#4a2c18"/>
        </linearGradient>
      </defs>
      <polygon points="0,0 375,0 332,63 375,127 0,127" fill="url(#ribbonFill)"/>
    </svg>
    <div class="brand">
      <div class="brand__mark"></div>
      <div class="brand__text">
        <div class="brand__name">BRACKENMOOR<br>GROUNDS</div>
        <div class="brand__tag">The Local Landscaping Experts</div>
      </div>
    </div>
  </div>
</section>

<section class="side side--back">
  <div class="mower-photo" role="img" aria-label="Photograph of a red ride-on mower cutting a striped green lawn"></div>

  <h1 class="headline">
    ALL OF YOUR<br>
    <span class="accent">LANDSCAPE</span> AND<br>
    GROUNDWORK <span class="accent">NEEDS...</span>
  </h1>

  <div class="intro">
    <p>Brackenmoor Grounds specialise in providing complete grounds maintenance and soft landscaping services to property and estate managers, housing associations, commercial and industrial sites, schools, hotels and nursing homes.</p>
    <p>We pride ourselves on delivering an excellent service based on your requirements. Our friendly team of trained and experienced staff will ensure your grounds are maintained beyond your expectations</p>
  </div>

  <div class="service-band">Ground Works | Landscaping | Garden Care</div>
  <div class="flower-photo flower-photo--beds" role="img" aria-label="Photograph of colourful planted flower borders"></div>
  <div class="flower-photo flower-photo--lawn" role="img" aria-label="Photograph of a neat lawn edged with pink flowering shrubs beside a house"></div>

  <div class="footer-panel">
    <div class="services-tab">
      <svg width="290" height="28" viewBox="0 0 290 28" aria-hidden="true"><polygon points="0,0 290,0 262,28 0,28" fill="#7ab533"/></svg>
      <span>Our Services Includes:</span>
    </div>

    <ul class="services">
      <li><svg width="11" height="11" viewBox="0 0 12 12" aria-hidden="true"><circle cx="6" cy="6" r="6" fill="#7ab533"/><path d="M3.2 6.2 5.2 8.1 8.9 4" stroke="#fff" stroke-width="1.6" fill="none"/></svg>Hedge &amp; Tree Surgery
        <span class="pair"><svg width="11" height="11" viewBox="0 0 12 12" aria-hidden="true"><circle cx="6" cy="6" r="6" fill="#7ab533"/><path d="M3.2 6.2 5.2 8.1 8.9 4" stroke="#fff" stroke-width="1.6" fill="none"/></svg>Fencing &amp; Decking</span></li>
      <li><svg width="11" height="11" viewBox="0 0 12 12" aria-hidden="true"><circle cx="6" cy="6" r="6" fill="#7ab533"/><path d="M3.2 6.2 5.2 8.1 8.9 4" stroke="#fff" stroke-width="1.6" fill="none"/></svg>Ground Clearance
        <span class="pair"><svg width="11" height="11" viewBox="0 0 12 12" aria-hidden="true"><circle cx="6" cy="6" r="6" fill="#7ab533"/><path d="M3.2 6.2 5.2 8.1 8.9 4" stroke="#fff" stroke-width="1.6" fill="none"/></svg>Earth Works</span></li>
      <li><svg width="11" height="11" viewBox="0 0 12 12" aria-hidden="true"><circle cx="6" cy="6" r="6" fill="#7ab533"/><path d="M3.2 6.2 5.2 8.1 8.9 4" stroke="#fff" stroke-width="1.6" fill="none"/></svg>Patios, Paths &amp; Driveways</li>
      <li><svg width="11" height="11" viewBox="0 0 12 12" aria-hidden="true"><circle cx="6" cy="6" r="6" fill="#7ab533"/><path d="M3.2 6.2 5.2 8.1 8.9 4" stroke="#fff" stroke-width="1.6" fill="none"/></svg>Mowing &amp; Garden Maintenance</li>
      <li><svg width="11" height="11" viewBox="0 0 12 12" aria-hidden="true"><circle cx="6" cy="6" r="6" fill="#7ab533"/><path d="M3.2 6.2 5.2 8.1 8.9 4" stroke="#fff" stroke-width="1.6" fill="none"/></svg>Pruning and leaf collection</li>
      <li><svg width="11" height="11" viewBox="0 0 12 12" aria-hidden="true"><circle cx="6" cy="6" r="6" fill="#7ab533"/><path d="M3.2 6.2 5.2 8.1 8.9 4" stroke="#fff" stroke-width="1.6" fill="none"/></svg>Garden design and layouts, Paving and Patios</li>
    </ul>

    <div class="brand">
      <div class="brand__mark"></div>
      <div class="brand__text">
        <div class="brand__name">BRACKENMOOR<br>GROUNDS</div>
        <div class="brand__tag">The Local Landscaping Experts</div>
      </div>
    </div>

    <ul class="contact">
      <li><svg width="11" height="11" viewBox="0 0 12 12" aria-hidden="true"><circle cx="6" cy="6" r="5.3" fill="none" stroke="#7ab533" stroke-width="1.3"/><ellipse cx="6" cy="6" rx="2.3" ry="5.3" fill="none" stroke="#7ab533" stroke-width="1"/><path d="M0.8 6H11.2" stroke="#7ab533" stroke-width="1"/></svg>www.brackenmoorgrounds.co.uk</li>
      <li><svg width="11" height="11" viewBox="0 0 12 12" aria-hidden="true"><rect x="0.7" y="2.2" width="10.6" height="7.6" fill="none" stroke="#7ab533" stroke-width="1.2"/><path d="M0.7 2.4 6 6.8 11.3 2.4" fill="none" stroke="#7ab533" stroke-width="1.2"/></svg>dale@brackenmoorgrounds.co.uk</li>
      <li><svg width="11" height="11" viewBox="0 0 12 12" aria-hidden="true"><path d="M3 1.2 5 3.6 3.9 5.1C4.6 6.6 5.5 7.5 7 8.2L8.4 7.1 10.8 9 9.6 10.8C5.4 10.8 1.2 6.6 1.2 2.4Z" fill="#7ab533"/></svg>07952 418260</li>
    </ul>
  </div>
</section>

</body>
</html>
```